Create the artwork for Velvetharbor's debut album, 'Where Rivers Bend Slowly'!

We are a cinematic pop/jazz quartet from Oslo/London looking for someone to create the artwork for our debutalbum, 'Where Rivers Bend Slowly'. This is a project we are incredibly proud of, and we are looking for the perfect artwork to complement our music.

We want the artwork to convey the organic feel of our sound, yet be eye-catching with bright colours. Attached are several examples for inspiration. The title of the album, 'Where Rivers Bend Slowly', should be an inspiration for the design in a subtle/abstract way. Think out of the box here, we are not looking for a hundred solar system designs.

You can find an album teaser here for inspiration: https://audiostreamhub.example/velvetharbormusic/album-teaser

This is our webpage: velvetharbormusic.example

Excited to see what you come up with and to work with some brilliant creatives !

Much love,

Velvetharbor
Updates

Everyone, thanks for your effort and great designs! We're discussing right now and will get back to you with feedback and suggested edits very shortly. Thanks for your patience! Much love, Velvetharbor

Requirements
Must have
• Ready-to-print high-res files in standard CD Cover format
• Artwork ready for digital release on tunewave, Songvault, and social media channels
Nice to have
• Would love to have smaller extensions of the artwork (pattern or pieces of art in same theme) to use on webpage/social media channels.

```html
<!DOCTYPE html>
<html lang="en">
<head>
<meta charset="utf-8">
<title>Velvetharbor — Where Rivers Bend Slowly</title>
<link rel="stylesheet" href="https://fonts.googleapis.com/css2?family=Libre+Baskerville&display=swap">
<style>
  :root {
    --sky-blue: #8fb1c6;
    --sky-deep: #7fa2b8;
    --maroon: #7a3f4a;
    --navy: #26304a;
    --cream: #fde6c3;
    --cream-light: #fee9c8;
    --title-slate: #4d6c84;
    --mark-white: #ffffff;
  }
  html, body {
    margin: 0;
    padding: 0;
    width: 1200px;
    height: 1200px;
    overflow: hidden;
    background: var(--cream-light);
  }
  .album-cover {
    position: relative;
    width: 1200px;
    height: 1200px;
    overflow: hidden;
    background: var(--cream-light);
  }
  .cover-artwork {
    position: absolute;
    left: 0;
    top: 0;
    width: 1200px;
    height: 1068px;
    background:
      radial-gradient(ellipse 300px 420px at 600px 520px, var(--navy) 0%, var(--maroon) 55%, rgba(122,63,74,0) 100%),
      linear-gradient(to bottom, var(--sky-blue) 0%, var(--sky-deep) 80%, var(--cream) 100%);
  }
  .band-mark {
    position: absolute;
    left: 40px;
    top: 700px;
    display: flex;
    align-items: center;
    gap: 14px;
    font-family: "Libre Baskerville", serif;
    font-size: 38px;
    color: var(--mark-white);
  }
  .band-mark-circle {
    width: 26px;
    height: 26px;
    border: 2px solid var(--mark-white);
    border-radius: 50%;
    flex: none;
  }
  .album-title {
    position: absolute;
    left: 0;
    top: 1082px;
    width: 1200px;
    margin: 0;
    text-align: center;
    font-family: "Libre Baskerville", serif;
    font-weight: 400;
    font-size: 30px;
    letter-spacing: 0.62em;
    color: var(--title-slate);
    white-space: nowrap;
  }
</style>
</head>
<body>
  <main class="album-cover">
    <div class="cover-artwork" role="img" aria-label="Collage artwork: a head-and-shoulders silhouette filled with a dense maroon and navy city collage, set against a pale blue city collage background fading into cream at the bottom"></div>
    <div class="band-mark">
      <span class="band-mark-circle"></span>
      <span class="band-mark-name">Velvetharbor</span>
    </div>
    <h1 class="album-title">WHERE RIVERS BEND SLOWLY</h1>
  </main>
</body>
</html>
```